Horseriders ecommerce

I need the design of a web site and ecommerce for horse riders product. the actual site is brinamarket.it and is completely to rebuild.
the most important thing that must come out from the design is that this shop sells products for both type of riding: english and western and as well has products available and good for both. (accessories and horse care)
the site owners loves much more the western riding and they want to gain a good part of customers of it, that's why i ask you to give the central area and importance to the western products.
at http://www.keltorange.com you can see a site style that we like, especially for the inner pages of products.
colors and graphics elements must be related to the world of horse riding, but we want the design to keep elegance and style, without being so western!
you need to find a way to create a cool design, user friendly to buy and that gives the real impression of professionality and care.
please check this site: http://www.pemblyworks.it/
the style is not so nice in my opinion, but somehow the navigation is friendly
in attachment to the project I add the mockup of the home page. Abou the inner page, please feel free to create the correct layout and check the one of www.keltorange.com which I like especially for the product sheet.

p.s. you can change the color of the logo
Updates

Hello dear designers,
i've pushed a little the deadline.
I will give you feedback in a while.
thaks to all
Ginevra

Target Market(s)

horse riders
western riders
english riders
stables owners

Industry/Entity Type

Product

Requirements
Must have
• style, elegance and western atmosphere. GOOD SPACES to show products.
• MUST HAVE a base way to manage banners in home page
Nice to have
• images of horses, but the most important images are products
Should not have
• too many western elements

```html
<!DOCTYPE html>
<html lang="it">
<head>
<meta charset="utf-8">
<title>BrinaShop – Horse Riders Store</title>
<link href="https://fonts.googleapis.com/css2?family=Oswald:wght@300;400;500&family=Tinos&family=Arimo:wght@400;700&family=Raleway:wght@200;400&display=swap" rel="stylesheet">
<style>
:root{
  --navy:#1b2a4a;
  --black:#050608;
  --paper:#e8e8e8;
  --brown:#6b2f22;
  --brown-head:#642b1e;
  --brown-item:#7f4738;
  --blue:#0d56b3;
  --blue-head:#0a4a9c;
  --blue-item:#2f79d2;
  --tan:#bcab8b;
  --tan-head:#ad9a76;
  --tan-item:#dcd1bb;
  --tan-text:#a38f73;
  --cream:#f3ece0;
  --pink:#e6cdc6;
  --white:#fff;
}
*{box-sizing:border-box;margin:0;padding:0}
html,body{width:934px;height:1200px;overflow:hidden}
body{position:relative;background:var(--black);font-family:"Arimo",sans-serif;color:var(--white)}
.abs{position:absolute}

.topbar{left:0;top:0;width:934px;height:31px;background:var(--navy);font-size:10.5px;display:flex;align-items:center;justify-content:flex-end;gap:15px;padding-right:56px}
.topbar .cart{display:flex;align-items:center;gap:6px}
.search{right:8px;top:5px}
.header{left:0;top:31px;width:934px;height:150px;background:var(--white);border-top:2px dashed var(--navy)}
.logo{left:13px;top:21px;width:166px;height:104px;display:flex;align-items:center;gap:8px;justify-content:center}
.logo .dot{width:22px;height:22px;border-radius:50%;background:var(--blue)}
.logo span{font-family:"Oswald",sans-serif;font-size:27px;color:var(--blue);font-weight:500}
.banner{left:204px;top:25px;width:498px;height:100px;border:4px solid var(--black);background:var(--brown)}
.banner .photo{height:63px;background:linear-gradient(90deg,#6d5444,#c9893f 30%,#8a6a50 60%,#d9b98c)}
.banner p{font-family:"Oswald",sans-serif;font-size:16px;text-align:center;line-height:29px;color:var(--white);font-weight:500}
.banner p small{font-size:12px}
.register{left:729px;top:25px;width:193px;height:56px;background:var(--blue);text-align:center;padding-top:7px}
.register b{display:block;font-family:"Oswald",sans-serif;font-size:22px;font-weight:500;line-height:24px}
.register em{font-style:normal;font-size:12.5px}
.share{top:90px;height:21px;width:90px;border-radius:3px;font-size:7px;display:flex;align-items:center;gap:6px;padding-left:6px}
.share i{width:9px;height:9px;background:var(--white);display:block}
.share.one{left:731px;background:#2f5fae}
.share.two{left:833px;background:#3fa7e6}

.nav{left:0;top:181px;width:934px;height:51px;font-family:"Oswald",sans-serif;font-size:21px;letter-spacing:-.5px}
.nav a{position:absolute;top:10px;transform:translateX(-50%);color:var(--white);text-decoration:none;white-space:nowrap;text-transform:uppercase}
.paper{left:0;top:343px;width:934px;height:477px;background:var(--paper)}
.footer{left:0;top:1100px;width:934px;height:100px;background:var(--navy);text-align:center;font-size:11.5px;padding-top:19px;color:#dde}
.cards{display:flex;justify-content:center;gap:3px;margin-top:14px}
.cards span{width:57px;height:35px;display:flex;align-items:center;justify-content:center;font-size:10px;font-weight:700}

.col{top:272px;width:296px;height:772px}
.col.english{left:24px;background:var(--brown)}
.col.western{left:319px;top:232px;height:848px;background:var(--blue)}
.col.care{left:615px;background:var(--tan)}
.col h2{font-family:"Oswald",sans-serif;font-weight:300;font-size:18px;text-align:center;height:40px;line-height:40px;text-transform:uppercase;letter-spacing:-.3px}
.english h2{background:var(--brown-head);color:#f1c9a8}
.western h2{background:var(--blue-head)}
.care h2{background:var(--tan-head);color:var(--cream)}
.menu{list-style:none;position:absolute;left:19px;width:259px;display:flex;flex-direction:column;gap:6px}
.english .menu,.care .menu{top:56px}
.western .menu{top:56px;left:17px}
.menu li{height:32px;line-height:30px;padding-left:14px;font-family:"Tinos",serif;font-size:14px;border-bottom:2px dotted rgba(255,255,255,.25);white-space:nowrap;overflow:hidden}
.english li{background:var(--brown-item)}
.western li{background:var(--blue-item)}
.care li{background:var(--tan-item);color:var(--tan-text);border-bottom-color:rgba(255,255,255,.6)}

.brands{left:19px;top:526px;width:259px;height:228px;background:#5d2619;display:grid;grid-template-columns:121px 121px;grid-auto-rows:67px;gap:6px;padding:7px}
.brands span{background:var(--pink);display:flex;align-items:center;justify-content:center;text-align:center;font-family:"Oswald",sans-serif;font-size:15px;color:#3a1c16;font-weight:500}

.saddle{left:17px;top:526px;width:261px;height:145px;background:var(--blue-head);padding:5px}
.saddle .art{width:100%;height:100%;background:linear-gradient(120deg,#5b97e0 40%,#8d5a3e 70%,#5a3322);border:1px dashed rgba(255,255,255,.5);position:relative}
.saddle b{position:absolute;font-family:"Oswald",sans-serif;font-weight:500;color:#11306b;left:20px;top:12px;font-size:22px;line-height:24px;letter-spacing:1px}
.saddle strong{position:absolute;right:14px;bottom:18px;font-family:"Oswald",sans-serif;font-size:31px;color:var(--white)}
.gift{left:17px;top:685px;width:261px;height:143px;background:var(--blue-head);padding:7px}
.gift div{height:100%;background:#d3e2f3;position:relative}
.gift h3{font-family:"Raleway",sans-serif;font-weight:200;font-size:44px;color:var(--blue-head);position:absolute;left:17px;top:14px;letter-spacing:-1px;white-space:nowrap}
.gift .buy{position:absolute;left:0;top:82px;width:223px;height:34px;background:var(--blue-head);font-size:12px;display:flex;align-items:center;padding-left:66px}
.gift .seal{position:absolute;left:8px;top:77px;width:46px;height:46px;border-radius:50%;background:#3e86dd;font-size:17px;display:flex;align-items:center;justify-content:center}

.news{left:18px;top:524px;width:260px;height:158px;background:var(--tan-head);padding:6px}
.post{height:70px;background:var(--cream);margin-bottom:5px;position:relative;border:1px dashed #c9b99a}
.post .cal{position:absolute;left:8px;top:5px;width:36px;height:58px;border-right:1px solid #c9b99a;text-align:center;font-family:"Oswald",sans-serif;color:#5a4a35}
.post .cal b{display:block;margin-top:12px;background:#6b5a43;color:var(--cream);font-size:16px;font-weight:400;height:26px;line-height:26px}
.post .cal i{font-style:normal;font-size:12px}
.post h4{position:absolute;left:53px;top:7px;font-family:"Oswald",sans-serif;font-weight:400;font-size:17px;line-height:21px;color:#5a4a35;width:196px}
.post h4 span{display:block;white-space:nowrap;overflow:hidden;text-overflow:ellipsis}
.post p{position:absolute;left:53px;bottom:3px;font-size:9.5px;color:#5a4a35}
.stables{left:18px;top:694px;width:260px;height:65px;background:var(--tan-head);padding:5px}
.stables div{height:100%;background:linear-gradient(90deg,#4a4036,#b8a88f 50%,#6e6050);position:relative}
.stables span{position:absolute;right:0;top:16px;background:rgba(170,150,115,.92);font-family:"Oswald",sans-serif;font-size:13px;padding:5px 12px}
</style>
</head>
<body>
<div class="abs topbar">
  <span>Contact Us</span><span>My Account</span><span>Login</span>
  <span class="cart"><svg width="18" height="14" viewBox="0 0 18 14"><path d="M1 1h3l2 8h9l2-6H5" fill="none" stroke="#fff" stroke-width="1.4"/><circle cx="7" cy="12" r="1.3" fill="#fff"/><circle cx="14" cy="12" r="1.3" fill="#fff"/></svg>Cart</span>
  <span>$0.00</span><span>0 Items</span>
</div>
<svg class="abs search" width="20" height="20" viewBox="0 0 20 20"><circle cx="8" cy="8" r="6" fill="none" stroke="#fff" stroke-width="2"/><path d="M12.5 12.5 18 18" stroke="#fff" stroke-width="2.4"/></svg>

<div class="abs header">
  <div class="abs logo"><i class="dot"></i><span>BrinaShop</span></div>
  <div class="abs banner">
    <div class="photo" role="img" aria-label="Tooled leather western saddle close-up"></div>
    <p>SADDLES ON SALE! <small>CHECK OUR ITEMS IN SALE</small></p>
  </div>
  <div class="abs register"><b>REGISTER NOW!</b><em>get a Bday Discount</em></div>
  <div class="abs share one"><i></i>Share on Pagebook</div>
  <div class="abs share two"><i></i>Share on Chirper</div>
</div>

<nav class="abs nav">
  <a style="left:81px">Who we are</a>
  <a style="left:254px">How to buy</a>
  <a style="left:439px">Special offers</a>
  <a style="left:619px">Payments</a>
  <a style="left:821px">blogsellaovest.it</a>
</nav>

<div class="abs paper"></div>

<section class="abs col english">
  <h2>English riders &amp; horses</h2>
  <ul class="menu">
    <li>RISERVATO AI MANEGGI</li><li>ABBIGLIAMENTO</li><li>SELLE E ACCESSORI</li><li>SOTTOPANCIA</li>
    <li>RISERVATO AI MANEGGI</li><li>ABBIGLIAMENTO</li><li>SELLE E ACCESSORI</li><li>SOTTOPANCIA</li>
    <li>RISERVATO AI MANEGGI</li><li>ABBIGLIAMENTO</li><li>SELLE E ACCESSORI</li><li>SOTTOPANCIA</li>
  </ul>
  <div class="abs brands">
    <span>Ferrandi Hats</span><span>Velbrook Boots</span>
    <span>Swift Loop</span><span>Mesa Ropes</span>
    <span>Tallgrass</span><span>Dustline</span>
  </div>
</section>

<section class="abs col western">
  <h2>Western riders &amp; horses</h2>
  <ul class="menu">
    <li>SOTTOPANCIA</li><li>SOTTOSELLA E ACCESSORI</li><li>MORSI E FILETTI</li><li>EQUIPAGGIAMENTO DEL CAVA</li>
    <li>PROTEZIONI PER CAVALLO</li><li>SOTTOSELLA E ACCESSORI</li><li>MORSI E FILETTI</li><li>EQUIPAGGIAMENTO DEL CAVA</li>
    <li>PROTEZIONI PER CAVALLO</li><li>SOTTOSELLA E ACCESSORI</li><li>MORSI E FILETTI</li><li>EQUIPAGGIAMENTO DEL CAVA</li>
  </ul>
  <div class="abs saddle">
    <div class="art" role="img" aria-label="Brown western saddle on a blue background">
      <b>BUILD YOUR<br>OWN SADDLE</b><strong>CLICK HERE</strong>
    </div>
  </div>
  <div class="abs gift"><div>
    <h3>GIFT CARD</h3>
    <span class="buy">FOR FAMILY &amp; FRIENDS</span>
    <span class="seal">BUY</span>
  </div></div>
</section>

<section class="abs col care">
  <h2>Accessories &amp; horsecare</h2>
  <ul class="menu">
    <li>EQUIPAGGIAMENTO DEL CAVA</li><li>CURA DEL CAVALLO</li><li>ARTICOLI PER SCUDERIA</li><li>RECINZIONI ELETTRICHE</li>
    <li>EQUIPAGGIAMENTO DEL CAVA</li><li>CURA DEL CAVALLO</li><li>ARTICOLI PER SCUDERIA</li><li>RECINZIONI ELETTRICHE</li>
    <li>EQUIPAGGIAMENTO DEL CAVA</li><li>CURA DEL CAVALLO</li><li>ARTICOLI PER SCUDERIA</li><li>RECINZIONI ELETTRICHE</li>
  </ul>
  <div class="abs news">
    <article class="post"><div class="cal"><b>01</b><i>FEB</i></div><h4><span>LOREM IPSUM DOLOR SIT</span><span>AMET, CONSECTETUR ADI...</span></h4><p>read more</p></article>
    <article class="post"><div class="cal"><b>31</b><i>JAN</i></div><h4><span>SED UT PERSPICIATIS, UNDE</span><span>OMNIS ISTE NATU</span></h4><p>read more</p></article>
  </div>
  <div class="abs stables"><div role="img" aria-label="Interior of horse stables with stalls"><span>PRODUCT STABLES</span></div></div>
</section>

<footer class="abs footer">
  <p>Copyright ©2012 La Selleria di Marco Vendelli – tutti i diritti riservati – P.IVA 03218476150</p>
  <div class="cards">
    <span style="background:#1c3c7a">CirclePay</span>
    <span style="background:#fff;color:#1c3c7a">Vantix</span>
    <span style="background:#2e7fd0">Amberline</span>
  </div>
</footer>
</body>
</html>
```